Business Card Design

Rubber roller servicing company. Specializing in rubber to metal bonding. Serving various industries including, pharmaceutical, textile, plastic extrusion, polythene bag converting, laminating and the food industries.

Industry/Entity Type

Plastic

Contact Information for Business Card

Carwick Roller & Rubber Co Ltd, Trevor Ambleside, Managing Director, Unit at Fernholt, Ridley Lane, Oxenby, Huddersfield, Westholm Shire, HX4 9TJ, Tel 01632 960481, Fax 01632 960527, email info@carwickroller.example.co.uk,

```html
<!DOCTYPE html>
<html lang="en">
<head>
<meta charset="utf-8">
<title>Carwick Roller &amp; Rubber Co Ltd – Business Card</title>
<link rel="stylesheet" href="https://fonts.googleapis.com/css2?family=Arimo:wght@400;700&family=Carlito&display=swap">
<style>
  :root {
    --page: #ffffff;
    --page-edge: #e6e6e6;
    --card: #fdfdfd;
    --card-edge: #e4e4e4;
    --accent: #a0a62e;
    --accent-text: #a3ae35;
    --ink: #8e8f91;
    --ink-soft: #6e6f71;
    --ink-body: #7a7b7d;
  }
  * { margin: 0; padding: 0; box-sizing: border-box; }
  html, body {
    width: 1200px; height: 901px; overflow: hidden;
    background: var(--page);
  }
  .canvas {
    position: relative; width: 1200px; height: 901px;
    border: 1px solid var(--page-edge);
    font-family: "Arimo", Arial, sans-serif;
  }
  .card {
    position: absolute; left: 95px; top: 144px;
    width: 1012px; height: 615px;
    background: var(--card);
    border: 2px solid var(--card-edge);
  }
  .card__band {
    position: absolute; left: -2px; top: -2px;
    width: 36px; height: 615px;
    background: var(--accent);
  }
  .wordmark {
    position: absolute; left: 97px; top: 30px;
    font-size: 60px; font-weight: 400; line-height: 1.1;
    color: var(--ink); white-space: nowrap;
  }
  .tagline {
    position: absolute; left: 96px; top: 197px;
    font-family: "Carlito", Calibri, sans-serif;
    font-size: 33px; letter-spacing: 2px; color: var(--ink-soft);
    line-height: 1; white-space: nowrap;
  }
  .person { position: absolute; left: 100px; line-height: 1; white-space: nowrap; }
  .person__name { top: 412px; font-size: 30px; color: var(--ink-body); }
  .person__role { top: 455px; font-size: 19px; color: var(--accent-text); }
  .divider {
    position: absolute; left: 414px; top: 353px;
    width: 9px; height: 186px; background: var(--accent);
  }
  .contact__icon { position: absolute; fill: var(--accent); }
  .contact__text {
    position: absolute; font-size: 23px; color: var(--ink-body);
    line-height: 1; white-space: nowrap;
  }
  .contact__text--address { font-size: 22px; letter-spacing: 0.3px; }
</style>
</head>
<body>
<div class="canvas">
  <section class="card">
    <div class="card__band"></div>

    <div class="wordmark">Carwick Roller<br>&amp; Rubber Co Ltd</div>

    <p class="tagline">Precision rubber roller and bond repair</p>

    <div class="person person__name">Trevor Ambleside</div>
    <div class="person person__role">Managing Director</div>

    <div class="divider"></div>

    <div class="contact">
      <svg class="contact__icon" style="left:490px;top:320px" width="24" height="30" viewBox="0 0 24 30" aria-hidden="true">
        <path d="M4 1 L9 1 L11 8 L7 10 C8 15 11 20 15 23 L18 19 L24 23 L22 29 C12 29 2 18 1 6 Z"/>
      </svg>
      <div class="contact__text" style="left:550px;top:326px">01632 960481</div>

      <svg class="contact__icon" style="left:489px;top:381px" width="34" height="30" viewBox="0 0 34 30" aria-hidden="true">
        <rect x="8" y="0" width="18" height="8"/>
        <path d="M3 10 H31 A3 3 0 0 1 34 13 V23 H28 V18 H6 V23 H0 V13 A3 3 0 0 1 3 10 Z"/>
        <path d="M8 20 H26 V30 H8 Z M11 23 V25 H23 V23 Z M11 27 V28 H23 V27 Z" fill-rule="evenodd"/>
      </svg>
      <div class="contact__text" style="left:555px;top:386px">01632 960527</div>

      <svg class="contact__icon" style="left:489px;top:446px" width="33" height="24" viewBox="0 0 33 24" aria-hidden="true">
        <path d="M0 0 H33 V24 H0 Z M3 3 V21 H30 V3 Z M3 3 L16.5 14 L30 3 L30 6 L16.5 17 L3 6 Z M3 21 L12 12 L13.5 13.5 L5 21 Z M30 21 L21 12 L19.5 13.5 L28 21 Z" fill-rule="evenodd"/>
      </svg>
      <div class="contact__text" style="left:547px;top:444px">info@carwickroller.example.co.uk</div>

      <svg class="contact__icon" style="left:494px;top:507px" width="24" height="33" viewBox="0 0 24 33" aria-hidden="true">
        <path d="M12 0 A12 12 0 0 1 24 12 C24 20 12 33 12 33 C12 33 0 20 0 12 A12 12 0 0 1 12 0 Z M12 7 A5 5 0 1 0 12 17 A5 5 0 1 0 12 7 Z" fill-rule="evenodd"/>
      </svg>
      <div class="contact__text contact__text--address" style="left:543px;top:509px">Unit at Fernholt, Ridley Lane, Oxenby,</div>
      <div class="contact__text contact__text--address" style="left:543px;top:556px">Dunmere, Westholm Shire, HX4 9TJ</div>
    </div>
  </section>
</div>
</body>
</html>
```